Looking for a clean, modern, and professional business card design that reflects Valtrin Systems

The design should include the company logo, contact details, and align with our brand identity. Please use a sophisticated and minimalist style, incorporating [specific colors, if applicable]. Creativity is welcome, but the card must maintain a polished and professional appearance.

Details to Include:

Name: Dario Velmonte
Title: VP Sales / Operations
Company: Valtrin Systems
Phone: 304.555.0147
Email: dario@valtrinsystems.example
Website: www.valtrinsystems.example

```html
<!DOCTYPE html>
<html lang="en">
<head>
<meta charset="utf-8">
<title>Valtrin Systems – Business Card</title>
<link href="https://fonts.googleapis.com/css2?family=Roboto:wght@400;500;700&display=swap" rel="stylesheet">
<style>
  :root {
    --page-bg: #cfd3d5;
    --paper: #f1f1ef;
    --ink: #111214;
    --brand-blue: #1d43a0;
    --band-text: #c8d2ea;
    --text-grey: #2a2a2a;
    --divider: #c9c9c6;
    --card-black: #151617;
    --reverse-ink: #eceeee;
  }
  * { box-sizing: border-box; margin: 0; padding: 0; }
  html, body {
    width: 1200px; height: 1050px; overflow: hidden;
    background: var(--page-bg);
    font-family: "Roboto", Arial, sans-serif;
  }
  .card {
    position: absolute; left: 180px; width: 840px; height: 480px;
    overflow: hidden; box-shadow: 0 10px 30px rgba(0,0,0,.18);
  }
  /* Front */
  .card-front { top: 25px; background: var(--paper); }
  .logo {
    position: absolute; left: 70px; top: 120px; width: 330px;
    display: flex; align-items: center; gap: 14px;
  }
  .logo-square { width: 22px; height: 22px; background: var(--brand-blue); flex: none; }
  .logo-name {
    font-weight: 700; font-size: 30px; letter-spacing: 3px;
    text-transform: uppercase; color: var(--ink); line-height: 1.1;
  }
  .divider {
    position: absolute; left: 430px; top: 90px; width: 1px; height: 170px;
    background: var(--divider);
  }
  .contact { position: absolute; left: 462px; top: 96px; }
  .person-name {
    font-weight: 700; font-size: 27px; text-transform: uppercase;
    color: var(--ink); letter-spacing: .5px;
  }
  .person-title { font-size: 21px; color: var(--brand-blue); margin-top: 2px; }
  .contact-list { list-style: none; margin-top: 16px; }
  .contact-list li {
    display: flex; align-items: center; gap: 12px;
    font-size: 20px; color: var(--text-grey); line-height: 31px; white-space: nowrap;
  }
  .contact-list svg { width: 18px; height: 18px; flex: none; }
  .band {
    position: absolute; left: 0; top: 350px; width: 840px; height: 64px;
  }
  .band-label {
    position: absolute; left: 0; top: 350px; width: 620px; height: 64px;
    display: flex; align-items: center; justify-content: center;
    color: var(--band-text); font-size: 17px; letter-spacing: 5px; text-transform: uppercase;
  }
  /* Back */
  .card-back { top: 545px; background: var(--card-black); }
  .back-logo {
    position: absolute; inset: 0;
    display: flex; flex-direction: column; align-items: center; justify-content: center; gap: 30px;
  }
  .back-name {
    display: flex; align-items: center; gap: 20px;
    font-weight: 700; font-size: 54px; letter-spacing: 6px;
    text-transform: uppercase; color: var(--reverse-ink);
  }
  .back-name .logo-square { width: 34px; height: 34px; }
  .back-tagline {
    font-size: 18px; letter-spacing: 6px; text-transform: uppercase; color: var(--reverse-ink);
  }
</style>
</head>
<body>

<section class="card card-front">
  <div class="logo">
    <span class="logo-square"></span>
    <span class="logo-name">Valtrin Systems</span>
  </div>

  <div class="divider"></div>

  <div class="contact">
    <p class="person-name">Dario Velmonte</p>
    <p class="person-title">VP Sales / Operations</p>
    <ul class="contact-list">
      <li>
        <svg viewBox="0 0 24 24"><path fill="var(--brand-blue)" d="M6.6 10.8a15.1 15.1 0 0 0 6.6 6.6l2.2-2.2a1 1 0 0 1 1-.25 11.4 11.4 0 0 0 3.6.57 1 1 0 0 1 1 1V20a1 1 0 0 1-1 1A17 17 0 0 1 3 4a1 1 0 0 1 1-1h3.5a1 1 0 0 1 1 1c0 1.25.2 2.45.57 3.57a1 1 0 0 1-.25 1z"/></svg>
        304.555.0147
      </li>
      <li>
        <svg viewBox="0 0 24 24"><path fill="var(--brand-blue)" d="M2 5h20v14H2z"/><path fill="none" stroke="var(--paper)" stroke-width="1.8" d="M2.5 5.5 12 13l9.5-7.5"/></svg>
        dario@valtrinsystems.example
      </li>
      <li>
        <svg viewBox="0 0 24 24"><circle cx="12" cy="12" r="10" fill="var(--brand-blue)"/><path fill="none" stroke="var(--paper)" stroke-width="1.4" d="M2 12h20M12 2c3 3 3 17 0 20M12 2c-3 3-3 17 0 20"/></svg>
        www.valtrinsystems.example
      </li>
    </ul>
  </div>

  <svg class="band" viewBox="0 0 840 64" preserveAspectRatio="none" aria-hidden="true">
    <polygon points="0,0 645,0 620,64 0,64" fill="var(--brand-blue)"/>
    <polygon points="655,0 840,0 840,64 630,64" fill="var(--ink)"/>
  </svg>
  <div class="band-label">Valtrin Systems</div>
</section>

<section class="card card-back">
  <div class="back-logo">
    <div class="back-name"><span class="logo-square"></span>Valtrin Systems</div>
    <p class="back-tagline">Valtrin Systems</p>
  </div>
</section>

</body>
</html>
```